"VelTra" - Ketamine Clinic - Save Minds and Heal Hearts!! -

I need a very nice modern happy brain themed warm website design for our cutting edge modern and caring ketamine IV infusion clinic that also offers talk therapy and telemedicine visits.
A great design using the color schemes in out logos (grey, white, purples and that need metallic fading colored effect in the logo).

```html
<!DOCTYPE html>
<html lang="en">
<head>
<meta charset="UTF-8">
<title>VelTra – Ketamine Clinic</title>
<link href="https://fonts.googleapis.com/css2?family=Kumbh+Sans:wght@600;700;800&family=Mulish:wght@400;600;700&display=swap" rel="stylesheet">
<style>
:root{
  --indigo:#3a0aa8;
  --violet:#7a1fe6;
  --purple-deep:#2d0a8c;
  --cyan:#0fb4e6;
  --cyan-ring:#12b6e8;
  --ink:#3b0c9e;
  --text:#2b2b3a;
  --white:#ffffff;
  --lavender:#dcc8f4;
  --pale:#f3f7fb;
}
*{margin:0;padding:0;box-sizing:border-box}
html,body{width:1200px;height:3840px;overflow:hidden}
body{position:relative;background:var(--white);font-family:"Mulish",sans-serif;color:var(--text)}
.abs{position:absolute}
.bg-shapes{position:absolute;left:0;top:0;width:1200px;height:3840px}

/* header */
.site-header{position:absolute;left:0;top:0;width:1200px;height:116px;border-radius:0 0 22px 22px;
  background:linear-gradient(90deg,var(--indigo),var(--violet) 50%,var(--cyan));border:3px solid var(--white);border-top:none;z-index:5}
.brand{position:absolute;display:flex;align-items:center;gap:8px;font-family:"Kumbh Sans",sans-serif;font-weight:800;color:var(--white)}
.brand-dot{border-radius:50%;background:var(--white)}
.site-header .brand{left:112px;top:36px;font-size:26px}
.site-header .brand-dot{width:18px;height:18px}
.main-nav{position:absolute;left:505px;top:50px;display:flex;gap:0}
.main-nav a{color:var(--white);text-decoration:none;font-size:15px;margin-right:36px}

/* hero */
.hero-visual{left:0;top:0;width:1200px;height:775px;border-radius:0 0 0 220px;
  background:radial-gradient(ellipse 330px 260px at 610px 300px,#2f54e8 0%,#1a2bb0 40%,#0a0c3a 75%,#04040f 100%)}
.hero-hand{left:240px;top:520px;width:560px;height:200px;border-radius:50%;
  background:radial-gradient(ellipse at center,rgba(214,40,110,.75),rgba(120,30,160,.3) 60%,transparent 75%)}
.hero-title{left:0;top:322px;width:1200px;text-align:center;font-family:"Kumbh Sans",sans-serif;font-weight:800;font-size:52px;line-height:52px;color:var(--white)}
.btn{position:absolute;display:flex;align-items:center;justify-content:center;border-radius:24px;font-size:17px;color:var(--white);text-decoration:none}
.btn-outline{border:1.5px solid var(--white)}
.btn-fill{background:linear-gradient(90deg,var(--indigo),var(--violet) 60%,var(--cyan))}

/* photos */
.photo{position:absolute;border-radius:50%;border:4px solid var(--cyan-ring);padding:8px;background:var(--white)}
.photo-fill{width:100%;height:100%;border-radius:50%}

.section-title{position:absolute;font-family:"Kumbh Sans",sans-serif;font-weight:700;font-size:36px;color:var(--ink)}
.body-copy{position:absolute;width:482px;font-size:17px;line-height:29px;text-align:justify}

.condition-label{position:absolute;width:260px;text-align:center;font-family:"Kumbh Sans",sans-serif;font-weight:700;font-size:19px;color:var(--ink)}

.play{position:absolute;left:836px;top:2394px;width:56px;height:56px;border-radius:50%;background:var(--purple-deep)}

/* testimonials */
.review{position:absolute;top:2968px;width:434px;height:247px;border:4px solid var(--cyan-ring);border-radius:40px;background:var(--pale);padding:44px 28px 0 28px}
.review p{font-size:16.5px;line-height:29px;text-align:justify;color:#333}
.review h4{margin-top:10px;font-family:"Kumbh Sans",sans-serif;font-size:17px;color:#111}
.stars{display:flex;gap:3px;margin-top:4px}
.avatar{position:absolute;right:36px;bottom:-58px;width:118px;height:118px;border-radius:50%;border:4px solid var(--cyan-ring);padding:6px;background:var(--white)}
.arrow{position:absolute;top:3082px;width:26px;height:26px}
.dots{position:absolute;left:565px;top:3323px;display:flex;gap:7px}
.dots span{width:12px;height:12px;border-radius:50%;border:2px solid var(--ink)}
.dots span.on{background:var(--ink)}

/* footer */
.footer-badge{left:558px;top:3443px;width:84px;height:84px;border-radius:50%;background:var(--white);border:4px solid var(--cyan-ring);display:flex;align-items:center;justify-content:center}
.follow{left:568px;top:3620px;font-family:"Kumbh Sans",sans-serif;font-weight:700;font-size:17px;color:var(--white)}
.social{position:absolute;top:3616px;width:28px;height:28px;border-radius:50%;background:rgba(255,255,255,.9)}
.footer-nav-band{left:0;top:3700px;width:860px;height:50px;border-radius:0 24px 24px 0;background:rgba(255,255,255,.12)}
.footer-nav{position:absolute;left:142px;top:3713px;display:flex}
.footer-nav a{color:var(--white);font-size:17px;text-decoration:none;margin-right:40px}
.footer-rule{left:111px;top:3763px;width:977px;height:1px;background:rgba(255,255,255,.5)}
.copyright{left:0;top:3796px;width:1200px;text-align:center;font-size:14px;color:var(--white)}
</style>
</head>
<body>

<!-- hero backdrop -->
<div class="abs hero-visual"></div>
<div class="abs hero-hand" role="img" aria-label="Glowing blue brain held above an open hand"></div>

<!-- wave bands -->
<svg class="bg-shapes" viewBox="0 0 1200 3840" aria-hidden="true">
  <defs>
    <linearGradient id="bandAbout" x1="0" y1="0" x2="1" y2="0">
      <stop offset="0" stop-color="#3a0aa8"/>
      <stop offset=".5" stop-color="#7a1fe6"/>
      <stop offset="1" stop-color="#0fb4e6"/>
    </linearGradient>
    <linearGradient id="bandInfusion" x1="0" y1="0" x2="1" y2="0">
      <stop offset="0" stop-color="#d5c2f0"/>
      <stop offset=".6" stop-color="#e2d0f8"/>
      <stop offset="1" stop-color="#cdeaf8"/>
    </linearGradient>
    <linearGradient id="bandFooter" x1="0" y1="0" x2="1" y2="0">
      <stop offset="0" stop-color="#3a0aa8"/>
      <stop offset=".5" stop-color="#7a1fe6"/>
      <stop offset="1" stop-color="#0fb4e6"/>
    </linearGradient>
  </defs>
  <path d="M0,960 C300,850 500,770 800,725 C1000,698 1150,700 1200,705 L1200,1305 C1000,1262 820,1260 660,1282 C420,1320 160,1430 0,1525 Z" fill="url(#bandAbout)"/>
  <path d="M0,2130 C300,2070 520,2080 720,2112 C920,2145 1100,2200 1200,2240 L1200,2910 C1000,2800 820,2735 620,2722 C400,2708 200,2690 0,2692 Z" fill="url(#bandInfusion)"/>
  <path d="M0,3745 C200,3600 420,3500 700,3470 C900,3452 1100,3440 1200,3438 L1200,3840 L0,3840 Z" fill="url(#bandFooter)"/>
</svg>

<!-- header -->
<header class="site-header">
  <div class="brand"><span class="brand-dot"></span>VelTra</div>
  <nav class="main-nav">
    <a href="#">Home</a><a href="#">Ketamine IV Infusion</a><a href="#">About Us</a><a href="#">Services</a><a href="#">News</a><a href="#">Contact</a>
  </nav>
</header>

<h1 class="abs hero-title">SAVE MINDS AND<br>HEAL HEARTS!!</h1>
<a class="btn btn-outline" href="#" style="left:519px;top:445px;width:161px;height:42px">Get Started</a>

<!-- about -->
<div class="photo" style="left:98px;top:800px;width:480px;height:480px">
  <div class="photo-fill" role="img" aria-label="Patient relaxing in a recliner during an IV infusion with a nurse" style="background:linear-gradient(135deg,#f1f1f1,#dcdcdc 60%,#c8c8c8)"></div>
</div>
<h2 class="section-title" style="left:607px;top:812px;color:var(--white)">About Us</h2>
<p class="body-copy" style="left:607px;top:876px;color:var(--white)">Lorem ipsum dolor sit amet, consectetur adipiscing elit, sed do eiusmod tempor incididunt ut labore et dolore magna aliqua. Quis ipsum suspendisse ultrices gravida. Risus commodo viverra maecenas accumsan lacus vel facilisis. Lorem ipsum dolor sit amet, consectetur adipiscing elit, sed do eiusmod tempor incididunt ut labore et dolore magna aliqua. Quis ipsum suspendisse ultrices gravida. Risus commodo viverra maecenas accumsan lacus vel facilisis.</p>
<a class="btn btn-outline" href="#" style="left:609px;top:1137px;width:162px;height:42px">Read More</a>

<!-- conditions -->
<h2 class="section-title" style="left:0;top:1512px;width:1200px;text-align:center">Ketamine Can Successfully Treat</h2>
<div class="photo" style="left:82px;top:1622px;width:232px;height:232px"><div class="photo-fill" role="img" aria-label="Woman holding her head in distress" style="background:linear-gradient(135deg,#5a4e44,#1f4a32)"></div></div>
<div class="photo" style="left:356px;top:1622px;width:232px;height:232px"><div class="photo-fill" role="img" aria-label="Man sitting with hands clasped in worry" style="background:linear-gradient(135deg,#e8e6e2,#a89884)"></div></div>
<div class="photo" style="left:630px;top:1622px;width:232px;height:232px"><div class="photo-fill" role="img" aria-label="Woman pressing her temples with a migraine" style="background:linear-gradient(135deg,#6a5a52,#2f2b2c)"></div></div>
<div class="photo" style="left:905px;top:1622px;width:232px;height:232px"><div class="photo-fill" role="img" aria-label="Woman showing contrasting calm and distressed moods" style="background:linear-gradient(135deg,#f4f4f4,#c9c9cc)"></div></div>
<div class="condition-label" style="left:68px;top:1872px">Depression / Anxiety</div>
<div class="condition-label" style="left:342px;top:1872px">PTSD</div>
<div class="condition-label" style="left:612px;top:1872px">Migraine Headaches</div>
<div class="condition-label" style="left:891px;top:1872px">Bipolar Depression</div>
<a class="btn btn-fill" href="#" style="left:519px;top:1965px;width:161px;height:43px">View More</a>

<!-- infusion -->
<h2 class="section-title" style="left:112px;top:2214px">Ketamine IV Infusion</h2>
<p class="body-copy" style="left:113px;top:2274px;color:#333">Lorem ipsum dolor sit amet, consectetur adipiscing elit, sed do eiusmod tempor incididunt ut labore et dolore magna aliqua. Quis ipsum suspendisse ultrices gravida. Risus commodo viverra maecenas accumsan lacus vel facilisis. Lorem ipsum dolor sit amet, consectetur adipiscing elit, sed do eiusmod tempor incididunt ut labore et dolore magna aliqua. Quis ipsum suspendisse ultrices gravida. Risus commodo viverra maecenas accumsan lacus vel facilisis.</p>
<a class="btn btn-fill" href="#" style="left:115px;top:2538px;width:160px;height:42px">Learn More</a>
<div class="photo" style="left:626px;top:2182px;width:480px;height:480px">
  <div class="photo-fill" role="img" aria-label="Clinician preparing an IV line for a reclining patient" style="background:linear-gradient(135deg,#ece9e4,#cfc6bc 55%,#4a4a58)"></div>
</div>
<div class="play"><svg width="56" height="56" viewBox="0 0 56 56"><path d="M22 17 L40 28 L22 39 Z" fill="#fff"/></svg></div>

<!-- testimonials -->
<h2 class="section-title" style="left:0;top:2868px;width:1200px;text-align:center">Testimonials</h2>
<svg class="arrow" style="left:50px" viewBox="0 0 26 26"><path d="M17 4 L8 13 L17 22" fill="none" stroke="#111" stroke-width="3.5"/></svg>
<svg class="arrow" style="left:1124px" viewBox="0 0 26 26"><path d="M9 4 L18 13 L9 22" fill="none" stroke="#111" stroke-width="3.5"/></svg>

<article class="review" style="left:147px">
  <p>Lorem ipsum dolor sit amet, consectetur adipiscing elit, sed do eiusmod tempor incididunt ut labore et dolore magna aliqua. Quis ipsum suspendisse ultrices gravida.</p>
  <h4>Dana Fowler</h4>
  <div class="stars">
    <svg width="78" height="14" viewBox="0 0 78 14" fill="#3b0c9e"><g id="st"><path d="M7 0 L9 5 L14 5 L10 8.5 L11.5 14 L7 10.5 L2.5 14 L4 8.5 L0 5 L5 5 Z"/></g><use href="#st" x="16"/><use href="#st" x="32"/><use href="#st" x="48"/><use href="#st" x="64"/></svg>
  </div>
  <div class="avatar"><div class="photo-fill" role="img" aria-label="Reviewer portrait" style="background:linear-gradient(135deg,#9a7a62,#4a3a32)"></div></div>
</article>
<article class="review" style="left:619px">
  <p>Lorem ipsum dolor sit amet, consectetur adipiscing elit, sed do eiusmod tempor incididunt ut labore et dolore magna aliqua. Quis ipsum suspendisse ultrices gravida.</p>
  <h4>Dana Fowler</h4>
  <div class="stars">
    <svg width="78" height="14" viewBox="0 0 78 14" fill="#3b0c9e"><use href="#st"/><use href="#st" x="16"/><use href="#st" x="32"/><use href="#st" x="48"/><use href="#st" x="64"/></svg>
  </div>
  <div class="avatar"><div class="photo-fill" role="img" aria-label="Reviewer portrait" style="background:linear-gradient(135deg,#9a7a62,#4a3a32)"></div></div>
</article>
<div class="dots"><span></span><span></span><span class="on"></span><span></span></div>

<!-- footer -->
<div class="abs footer-badge"><span class="brand-dot" style="width:30px;height:30px;background:var(--violet);display:block"></span></div>
<div class="abs follow">FOLLOW US</div>
<span class="social" style="left:702px"></span>
<span class="social" style="left:744px"></span>
<span class="social" style="left:786px"></span>
<span class="social" style="left:831px"></span>
<div class="brand" style="left:930px;top:3640px;font-size:44px"><span class="brand-dot" style="width:26px;height:26px"></span>VelTra</div>
<div class="abs footer-nav-band"></div>
<nav class="footer-nav">
  <a href="#">Home</a><a href="#">Ketamine IV Infusion</a><a href="#">About Us</a><a href="#">Services</a><a href="#">News</a><a href="#">Contact</a>
</nav>
<div class="abs footer-rule"></div>
<div class="abs copyright">© Copyrights 2023 VelTra.com | All Rights Reserved</div>

</body>
</html>
```